Visitenkarten-Design für moderne Steuerberatung
Zielgruppe
Treuhandgesellschaft, Steuerberatung, Unternehmensberatung, Buchhaltung
Zielgruppe sind KMU und Privatpersonen
Aufgabenstellung
modern, schlicht, übersichtlich

```html
<!DOCTYPE html>
<html lang="de">
<head>
<meta charset="utf-8">
<title>Halvoren – Visitenkarten</title>
<link href="https://fonts.googleapis.com/css2?family=Ubuntu:wght@400;700&display=swap" rel="stylesheet">
<style>
  :root {
    --brand-blue: #233f94;
    --text-grey: #555a60;
    --fold-grey: #b9bcc0;
    --card-white: #ffffff;
    --canvas: #ffffff;
  }
  html, body {
    margin: 0;
    width: 1200px;
    height: 841px;
    overflow: hidden;
    background: var(--canvas);
  }
  .sheet {
    width: 1200px;
    height: 841px;
    display: flex;
    align-items: center;
    justify-content: center;
    gap: 60px;
  }
  .card-pair {
    display: flex;
    gap: 24px;
  }
  .card {
    width: 262px;
    height: 405px;
    display: block;
    background: var(--card-white);
    box-shadow: 0 2px 6px rgba(0,0,0,0.18);
    font-family: "Ubuntu", sans-serif;
  }
  .wordmark { font-family: "Ubuntu", sans-serif; font-weight: 700; fill: var(--brand-blue); }
  .tagline { font-family: "Ubuntu", sans-serif; font-weight: 400; fill: var(--text-grey); }
  .person-name { font-weight: 700; fill: var(--brand-blue); }
  .contact { font-weight: 400; fill: var(--text-grey); }
  .brand-dot { fill: var(--brand-blue); }
  .accent { fill: var(--brand-blue); }
  .fold-line { stroke: var(--fold-grey); stroke-width: 2; }
</style>
</head>
<body>
<main class="sheet">

  <!-- Variante Diagonale -->
  <section class="card-pair card-pair--diagonal">
    <svg class="card card--front" viewBox="0 0 388 600" aria-label="Vorderseite Variante Diagonale">
      <circle class="brand-dot" cx="194" cy="160" r="80"/>
      <line class="fold-line" x1="0" y1="456" x2="165" y2="356"/>
      <polygon class="accent" points="163,356 388,220 388,356"/>
      <text class="wordmark" x="194" y="525" font-size="42" text-anchor="middle">HALVOREN</text>
      <text class="tagline" x="194" y="548" font-size="18" text-anchor="middle">Treuhand &amp; Consulting</text>
    </svg>

    <svg class="card card--back" viewBox="0 0 388 600" aria-label="Rückseite Variante Diagonale">
      <text x="35" y="51" font-size="21" class="person-name">Jonas Berger</text>
      <text x="35" y="73" font-size="17" class="contact">Unternehmensberater</text>
      <text x="35" y="122" font-size="17" class="contact">Lindenweg 42</text>
      <text x="35" y="143" font-size="17" class="contact">Feldburg 48120</text>
      <text x="35" y="171" font-size="17" class="contact">Tel.: 0412 67890</text>
      <text x="35" y="192" font-size="17" class="contact">Fax.: 0412 67890</text>
      <text x="35" y="220" font-size="17" class="contact">office@Halvoren.de</text>
      <text x="35" y="242" font-size="17" class="contact">www.Halvoren.de</text>
      <line class="fold-line" x1="0" y1="270" x2="388" y2="505"/>
      <text class="wordmark" x="35" y="545" font-size="42">HALVOREN</text>
      <text class="tagline" x="35" y="567" font-size="18">Treuhand &amp; Consulting</text>
    </svg>
  </section>

  <!-- Variante Seitenband -->
  <section class="card-pair card-pair--band">
    <svg class="card card--front" viewBox="0 0 388 600" aria-label="Vorderseite Variante Seitenband">
      <rect class="accent" x="0" y="0" width="18" height="600"/>
      <circle class="brand-dot" cx="80" cy="120" r="76"/>
      <text class="wordmark" x="194" y="310" font-size="42" text-anchor="middle">HALVOREN</text>
      <text class="tagline" x="194" y="332" font-size="18" text-anchor="middle">Treuhand &amp; Consulting</text>
    </svg>

    <svg class="card card--back" viewBox="0 0 388 600" aria-label="Rückseite Variante Seitenband">
      <rect class="accent" x="0" y="0" width="18" height="600"/>
      <text x="53" y="51" font-size="21" class="person-name">Jonas Berger</text>
      <text x="53" y="73" font-size="17" class="contact">Unternehmensberater</text>
      <text x="53" y="122" font-size="17" class="contact">Lindenweg 42</text>
      <text x="53" y="143" font-size="17" class="contact">Feldburg 48120</text>
      <text x="53" y="171" font-size="17" class="contact">Tel.: 0412 67890</text>
      <text x="53" y="192" font-size="17" class="contact">Fax.: 0412 67890</text>
      <text x="53" y="220" font-size="17" class="contact">office@Halvoren.de</text>
      <text x="53" y="242" font-size="17" class="contact">www.Halvoren.de</text>
      <text class="wordmark" x="53" y="545" font-size="42">HALVOREN</text>
      <text class="tagline" x="53" y="567" font-size="18">Treuhand &amp; Consulting</text>
    </svg>
  </section>

</main>
</body>
</html>
```